Maplewood Surgery Brochure Design

Maplewood Surgery (maplewoodsurgery.example)

Is a comprehensive breast care center that focuses on caring for women with breast cancer and other breast pathologies. We need a promotional and marketing brochure, in a tri-fold format, to provide information about our office and describe the services that we offer.

Deliverable

* The brochure should be completed by August 24th
* We will need the necessary files to get the brochure printed (.ai, .indd, etc).

Target Market(s)

Primarily patients of age between 30+ and 70+. The brochure will also be placed in doctor's waiting room

Industry/Entity Type

Marketing

Requirements
Must have
• * Make use of the color scheme as the website (http://maplewoodsurgery.example, http://maplewoodsurgery.example/static/theme-fuchsia.png)
* Incorporate the following graphic elements:
* The company’s logo (provided as an attachment)
* At least one images from the homepage
* Photos of the primary doctor and her staff
* Map to show the office location and phone number
* Enclose a breast cancer self-exam card (http://maplewoodsurgery.example/static/shower-card.jpg)
* A portion of the brochure must be detachable and serve as business cards that can be cut off (see attachment).
Nice to have
• Here is an example of a brochure that we like:

http://designbazaro.example/item/flexible-trifold-brochure/318274?WT.ac=search_item&WT.seg_1=search_item&WT.z_author=mendavik

```html
<!DOCTYPE html>
<html lang="en">
<head>
<meta charset="utf-8">
<title>Maplewood Surgery – Brochure Inside Spread</title>
<link rel="stylesheet" href="https://fonts.googleapis.com/css2?family=Pinyon+Script&family=Open+Sans:wght@300;400;600&display=swap">
<style>
  :root {
    --magenta: #9c1d57;
    --magenta-deep: #84164a;
    --magenta-glow: #b23a72;
    --cream: #f6e6b8;
    --gold: #f1d98a;
    --white: #ffffff;
    --petal: #f2c9da;
    --petal-pale: #f7e4ec;
    --skin: #9a6650;
    --skin-deep: #7d4f3c;
  }
  * { margin: 0; padding: 0; box-sizing: border-box; }
  html, body { width: 1200px; height: 849px; overflow: hidden; background: var(--magenta); }
  .spread {
    position: relative; width: 1200px; height: 849px; overflow: hidden;
    background:
      linear-gradient(115deg, rgba(255,255,255,0) 30%, rgba(255,255,255,.06) 45%, rgba(255,255,255,0) 60%),
      radial-gradient(ellipse at 55% 25%, var(--magenta-glow) 0%, var(--magenta) 55%, var(--magenta-deep) 100%);
    font-family: "Open Sans", Arial, sans-serif; font-weight: 400; color: var(--white);
    font-size: 11.3px; line-height: 20px;
  }
  .fold { position: absolute; left: 810px; top: 0; height: 849px; border-left: 1.5px dashed rgba(255,255,255,.85); }

  .photo { position: absolute; }
  .photo--flowers-left {
    left: 0; top: 520px; width: 600px; height: 329px;
    background: linear-gradient(to top, rgba(242,201,218,.95) 0%, rgba(242,201,218,.7) 45%, rgba(242,201,218,0) 100%);
  }
  .photo--flowers-top {
    left: 1065px; top: 0; width: 135px; height: 85px;
    background: linear-gradient(to bottom left, var(--petal-pale) 0%, rgba(247,228,236,.6) 45%, rgba(247,228,236,0) 100%);
  }
  .photo--flowers-right {
    left: 910px; top: 650px; width: 290px; height: 199px;
    background: linear-gradient(to top left, rgba(242,201,218,.35) 0%, rgba(242,201,218,0) 100%);
  }
  .photo--woman {
    left: 565px; top: 485px; width: 230px; height: 364px;
    background: linear-gradient(to bottom, rgba(154,102,80,0) 0%, var(--skin) 22%, var(--skin-deep) 100%);
  }

  .panel { position: absolute; top: 32px; }
  .panel--left { left: 29px; width: 362px; }
  .panel--middle { left: 418px; width: 380px; }
  .panel--right { left: 833px; width: 345px; }
  .panel-title {
    font-family: "Pinyon Script", cursive; font-weight: 400; color: var(--cream);
    font-size: 56px; line-height: 64px; margin-bottom: 14px;
  }
  .panel--left .panel-title { padding-left: 38px; }
  .panel--middle .panel-title { padding-left: 115px; }
  .panel--right .panel-title { padding-left: 95px; }
  p { margin-bottom: 20px; }
  .label { color: var(--gold); text-transform: uppercase; }
  .label--plain { color: var(--white); font-weight: 600; text-transform: none; }
  .narrow { width: 160px; margin-top: -20px; }

  .doctor { display: flex; gap: 11px; margin-bottom: 14px; }
  .doctor-photo {
    flex: 0 0 96px; height: 120px;
    background: linear-gradient(170deg, #6a4a3a 0%, #4a3a30 50%, #6b604c 100%);
  }
  .doctor-bio p { margin-bottom: 12px; }
  .doctor-bio p:last-child { margin-bottom: 0; }
  .services-title { color: var(--gold); text-transform: uppercase; font-weight: 400; font-size: 11.3px; margin-bottom: 4px; }
  .services { list-style: none; margin-bottom: 16px; }
  .services li { position: relative; padding-left: 20px; }
  .services li::before { content: ""; position: absolute; left: 2px; top: 8px; width: 4px; height: 4px; border-radius: 50%; background: var(--white); }
</style>
</head>
<body>
<main class="spread">
  <div class="photo photo--flowers-left" role="img" aria-label="Pale pink lotus flowers with yellow centres"></div>
  <div class="photo photo--flowers-top" role="img" aria-label="Small pale flowers in the top corner"></div>
  <div class="photo photo--flowers-right" role="img" aria-label="Faint pink flower in the lower corner"></div>
  <div class="photo photo--woman" role="img" aria-label="Photo of a serene mature woman hugging her shoulders"></div>

  <div class="fold" aria-hidden="true"></div>

  <section class="panel panel--left">
    <h2 class="panel-title">Comprehensive</h2>
    <p>We provide a caring, intimate environment where your dignity and health come first. Conveniently, we are situated next to Brookfield Hospital, in the Whitcombe Harlow Cancer Center. This means that any necessary diagnostic and treatment modalities are at our fingertips.</p>
    <p>We understand the anxiety involved with breast problems. We know that when you are told that you need to be evaluated more closely, you want answers as quickly as possible. We are here to help you, striving to be as proficient as possible. Being dedicated to breast care, we have a wealth of up-to-date knowledge about current breast care concepts. Your doctor will listen to your concerns and work with you to make sure you understand your options.</p>
    <p>Our knowledgeable staff will help to alleviate your anxiety with timely appointments, education and compassion. We will make sure you have all the facts to make the best decisions about your health care.</p>
  </section>

  <section class="panel panel--middle">
    <h2 class="panel-title">Timely</h2>
    <p><span class="label">Dedicated</span> – to bringing to you the most fresh and knowledgeable breast care, including all diagnostic studies and any surgical techniques necessary.</p>
    <p><span class="label">Unified team approach</span> – one that includes communication with your primary doctor, laboratory, radiology and ancillary services in a coordinated effort.</p>
    <p><span class="label">Appropriate resources</span> – including support groups, therapy, oncology, radiation oncology, cancer societies and more.</p>
    <p><span class="label label--plain">Experience:</span> Dr. Marchetti has focused her entire practice on breast surgery, as she feels that this is the field in which she excels. Being fellowship-trained in Oncoplastic Breast Surgery, she intensely believes in comprehensive breast care and being with the patient through the entire experience. She is comfortable treating patients of all ages, from birth to the elderly. Being compassionate and caring, she strives to project these qualities into everything that she puts her hands on. Dr. Marchetti is passionate about making</p>
    <p class="narrow">sure that her patients get the best care, that they are well-informed, and treated with the dignity and respect that they deserve.</p>
  </section>

  <section class="panel panel--right">
    <h2 class="panel-title">Personal</h2>
    <div class="doctor">
      <div class="doctor-photo" role="img" aria-label="Portrait photo of Dr. Lena Marchetti"></div>
      <div class="doctor-bio">
        <p>Dr. Lena Marchetti is the first fellowship-trained breast surgeon south of Springfield, Ill., and is excited to come home and bring her expertise to the women of Southern Illinois.</p>
        <p>She deeply understands that you need to heal physically... emotionally... spiritually.</p>
      </div>
    </div>
    <p>This is truly comprehensive breast care.</p>
    <h3 class="services-title">Services include:</h3>
    <ul class="services">
      <li>Breast pain and other nonsurgical management of breast problems</li>
      <li>Treatment of diseases of the breast (abscesses, gynecomastia)</li>
      <li>Biopsies (including minimally invasive with ultrasound or stereotactic guidance)</li>
      <li>Cryoablation (freezing) of certain breast conditions</li>
      <li>Breast resections (as needed for benign or malignant disease processes)</li>
      <li>Lymph node resections (including sentinel lymph node excisions)</li>
      <li>Breast reconstruction and balancing of the “other” breast as needed</li>
      <li>Breast reductions (for cancer or for burdensome breasts)</li>
      <li>Mastopexies (breast lifts for cancer or droopy breasts)</li>
    </ul>
    <p>Of course, this is not an exhaustive list. If there is a procedure you are interested in, please call our office to find out if we offer it.</p>
  </section>
</main>
</body>
</html>
```